Content marketing firm needs a creative out of the box stationary design

Please take a look to the uploaded logo
I need the whole stationary package which include designs for (business card, letterhead, folder, notepad, company profile, small and big envelop, CD and its cover, key medal, header cover for social media pages "facebook, twitter, linkedin, insgram, google+" and website, favicon for website, E-mail signature, flyer, brochure)

```html
<!DOCTYPE html>
<html lang="en">
<head>
<meta charset="utf-8">
<title>Brightword Media — Envelope Dieline</title>
<link rel="stylesheet" href="https://fonts.googleapis.com/css2?family=Nunito:wght@900&display=swap">
<style>
  :root {
    --brand-blue: #25a9e0;
    --ink: #111111;
    --cut-line: #333333;
    --fold-line: #b3b3b3;
    --paper: #ffffff;
  }
  html, body {
    margin: 0;
    padding: 0;
    overflow: hidden;
    background: var(--paper);
  }
  .canvas {
    width: 1200px;
    height: 1020px;
    position: relative;
    overflow: hidden;
    background: var(--paper);
  }
  .dieline {
    position: absolute;
    left: 0;
    top: 0;
    width: 1200px;
    height: 1013px;
  }
  .flap-fill { fill: var(--brand-blue); }
  .cut { fill: none; stroke: var(--cut-line); stroke-width: 0.8; }
  .fold { fill: none; stroke: var(--fold-line); stroke-width: 1.2; stroke-dasharray: 5 4; }
  .notch { fill: var(--ink); }
  .brand-name {
    font-family: "Nunito", sans-serif;
    font-weight: 900;
    font-size: 26px;
    fill: var(--ink);
    letter-spacing: 0.5px;
  }
</style>
</head>
<body>
<main class="canvas">
  <svg class="dieline" viewBox="0 0 1440 1216" xmlns="http://www.w3.org/2000/svg" aria-label="Envelope dieline for Brightword Media">
    <!-- Open envelope: top flap -->
    <path class="flap-fill top-flap" d="M378,418 L395,383 Q400,376 410,373 L630,304 Q720,285 810,304 L1035,373 Q1045,377 1050,385 L1062,418 Z"/>

    <!-- Side flaps -->
    <path class="cut side-flap-left" d="M378,420 L160,488 Q136,497 137,512 Q137,522 145,529 L322,693 Q335,705 378,716"/>
    <path class="cut side-flap-right" d="M1062,420 L1280,488 Q1304,497 1303,512 Q1303,522 1295,529 L1118,693 Q1105,705 1062,716"/>

    <!-- Bottom flap -->
    <path class="cut bottom-flap" d="M378,716 L382,730 Q385,742 395,750 L575,925 Q580,931 590,931 L850,931 Q858,931 863,925 L1045,750 Q1055,742 1058,730 L1062,716"/>

    <!-- Body panel fold lines -->
    <rect class="fold body-panel" x="378" y="418" width="684" height="298"/>

    <!-- Corner notches -->
    <path class="notch" d="M368,408 L376,416 L372,404 Z"/>
    <path class="notch" d="M1072,408 L1064,416 L1068,404 Z"/>
    <path class="notch" d="M368,728 L376,718 L372,731 Z"/>
    <path class="notch" d="M1072,728 L1064,718 L1068,731 Z"/>

    <!-- Return address brand name -->
    <text class="brand-name" x="949" y="668" text-anchor="middle">BRIGHTWORD</text>

    <!-- Closed envelope preview -->
    <rect class="fold preview-body" x="1000" y="1006" width="385" height="167"/>
    <path class="flap-fill preview-flap" d="M1000,1006 L1385,1006 L1378,1022 Q1374,1030 1365,1033 L1245,1070 Q1192,1085 1140,1070 L1020,1033 Q1010,1030 1007,1022 Z"/>
  </svg>
</main>
</body>
</html>
```